Brellow Publishing

I made a website myself www.brellowpublishing.co.uk a few years ago but I need a new design, which I will code. One that I can be proud of, that 's sexy, to win new customers and showcase my publishing skills. This is a publishing website so I want the home page and books page to be fantastic. I have a logo already so will like the same colour scheme or thereabouts. I have current files and features that I would like to add to your creativity and experience.

Target Market(s)

Web Designers, Graphic Designers

Industry/Entity Type

Book Publisher

Number of Pages Required

5+ page

Font styles to use
Sans Serif

Colors
0255a3
ffffff
ec1f27

Requirements
Must have
• Menu and Sub Menu
• Footer
• Buy Page - Shopping Cart
• Upload feature on the submissions page
• video section on home page (how we publish books)
• Ad space section
Nice to have
• social media bar
• Zoom in page

```html
<!DOCTYPE html>
<html lang="en">
<head>
<meta charset="utf-8">
<title>Brellow Publishing — Home</title>
<link href="https://fonts.googleapis.com/css2?family=Open+Sans:wght@400;600;700;800&family=Cinzel:wght@400;600&display=swap" rel="stylesheet">
<style>
:root{
  --blue:#0255a3;
  --red:#ec1f27;
  --green:#8cc63f;
  --white:#ffffff;
  --ink:#333333;
  --grey-panel:#6b6b6b;
  --grey-band:#c9c9c9;
  --footer:#2b2b2b;
}
*{box-sizing:border-box;margin:0;padding:0}
html,body{width:1200px;height:3429px;overflow:hidden}
body{font-family:"Open Sans",Arial,sans-serif;color:var(--ink);background:var(--white);position:relative}
section,header,footer{position:relative;width:1200px}

/* Header */
.site-header{height:80px;background:var(--white)}
.brand{position:absolute;left:58px;top:14px;height:50px;width:240px;border:2px solid #d9d9d9;border-radius:6px;display:flex;align-items:center;gap:10px;padding-left:12px}
.brand-dot{width:22px;height:22px;border-radius:50%;background:var(--red)}
.brand-name{font-weight:700;font-size:20px;color:var(--blue);white-space:nowrap}
.nav-bar{position:absolute;left:340px;top:0;right:0;height:80px;background:var(--blue);border-radius:0 0 0 50px;display:flex;align-items:center;padding-left:30px}
.nav-bar a{color:var(--white);text-decoration:none;font-size:15px;font-weight:600;margin-right:34px}
.nav-bar a.active{color:var(--red)}
.nav-tools{display:flex;gap:20px;align-items:center;margin-left:4px}

/* Hero */
.hero{height:571px}
.hero-photo{position:absolute;inset:0;background:linear-gradient(100deg,#b8875a 0%,#e9e3da 35%,#d9d6d2 60%,#8d8a88 85%,#4a3b30 100%)}
.social-bar{position:absolute;left:0;top:149px;width:58px}
.social-bar span{display:flex;align-items:center;justify-content:center;height:63px}
.social-bar span:nth-child(1){background:var(--red)}
.social-bar span:nth-child(2){background:var(--green)}
.social-bar span:nth-child(3){background:var(--blue)}
.social-bar i{display:block;width:26px;height:26px;border:2px solid var(--white);border-radius:50%}
.social-toggle{position:absolute;left:58px;top:149px;width:32px;height:36px;background:#eee;color:#777;font-size:18px;display:flex;align-items:center;justify-content:center}
.hero-title{position:absolute;left:130px;top:182px;width:620px;text-align:center;font-family:"Cinzel",serif;color:#1d2f55;white-space:nowrap}
.hero-title h1{font-size:36px;line-height:44px;font-weight:400;letter-spacing:2px}
.hero-title p{font-size:24px;line-height:32px;letter-spacing:2px;margin-top:2px}
.btn-submit{position:absolute;left:339px;top:297px;width:200px;height:54px;background:var(--red);color:var(--white);font-weight:700;font-size:19px;display:flex;align-items:center;justify-content:center;letter-spacing:1px}

/* Intro */
.intro{height:538px;text-align:center}
.intro h2{padding-top:44px;color:var(--blue);font-size:30px;font-weight:700;letter-spacing:1px}
.intro p{width:820px;margin:28px auto 0;font-size:14px;line-height:20px;color:#444}
.feature-cards{position:absolute;top:222px;left:119px;display:flex;gap:112px}
.card{width:254px;height:247px;border-radius:0 36px 0 36px;display:flex;flex-direction:column;align-items:center;justify-content:center;gap:24px;font-weight:800;font-size:22px;letter-spacing:1px}
.card-books{border:3px solid var(--blue);color:var(--red);background:var(--white)}
.card-author{background:var(--red);color:var(--white)}
.card-submission{background:var(--green);color:var(--white)}

/* Video */
.video{height:365px}
.video-still{position:absolute;inset:0;background:linear-gradient(120deg,#6d6d6d,#cfcfcf 45%,#a8a8a8 70%,#5e5e5e)}
.play{position:absolute;left:534px;top:111px}
.video h2{position:absolute;width:100%;top:284px;text-align:center;color:var(--white);font-size:37px;font-weight:700;letter-spacing:1px}

/* Steps */
.steps{height:576px}
.step{position:absolute;width:300px;text-align:center}
.step h3{font-size:25px;font-weight:800;color:var(--blue);letter-spacing:1px;margin-top:12px}
.step p{font-size:12.5px;line-height:19px;color:#444;margin-top:10px}
.step-writing{left:56px;top:60px}
.step-review{left:56px;top:302px}
.step-submission{left:837px;top:60px}
.step-contract{left:837px;top:302px}
.steps-panel{position:absolute;left:373px;top:57px;width:454px;height:487px;background:var(--grey-panel);border:14px solid var(--white);box-shadow:0 0 0 3px #9a9a9a;padding:28px 24px;color:var(--white)}
.steps-panel h2{text-align:center;font-size:25px;font-weight:700;line-height:44px;letter-spacing:1px;white-space:nowrap}
.steps-panel h2 em{font-style:normal;color:var(--red)}
.steps-panel ul{list-style:none;margin-top:26px}
.steps-panel li{font-size:12.5px;line-height:21px;font-weight:600;padding-left:14px;position:relative;margin-bottom:4px}
.steps-panel li::before{content:"";position:absolute;left:0;top:8px;width:6px;height:6px;background:var(--red)}
.steps-panel .more{margin-top:28px;font-size:12.5px;font-weight:600;text-decoration:underline}
.steps-panel .more span{color:var(--red)}

/* Books */
.books{height:469px;background:var(--grey-band)}
.books h2{text-align:center;padding-top:36px;color:var(--white);font-size:30px;font-weight:700;letter-spacing:1px}
.book-row{position:absolute;top:121px;left:160px;display:flex;gap:48px}
.cover{width:186px;height:279px;border:3px solid #222;box-shadow:2px 4px 8px rgba(0,0,0,.4)}
.cover-1{background:linear-gradient(#7d1a1a,#5a0f10)}
.cover-2{background:linear-gradient(#2f3b56,#c98a3a 60%,#7a5a2c)}
.cover-3{background:linear-gradient(#c23a2a,#e8d9b8 40%,#6f8f5b)}
.cover-4{background:linear-gradient(#2a2a2a,#111)}
.arrow-btn{position:absolute;top:213px;width:64px;height:75px;background:#e3e3e3;display:flex;align-items:center;justify-content:center}
.arrow-prev{left:0}.arrow-next{right:0}

/* Testimonials */
.testimonials{height:265px}
.testimonials h2{text-align:center;padding-top:34px;color:var(--blue);font-size:30px;font-weight:700;letter-spacing:1px}
.avatar{position:absolute;left:212px;top:121px;width:100px;height:100px;border-radius:50%;background:linear-gradient(#c89d79,#7a5a42);border:4px solid var(--white)}
.quote-badge{position:absolute;left:170px;top:93px;width:66px;height:66px;border-radius:50%;background:var(--blue);color:var(--white);font-size:46px;font-weight:800;display:flex;align-items:center;justify-content:center;padding-top:20px}
.testimonial-text{position:absolute;left:377px;top:118px;width:680px;font-size:16px;line-height:28px;color:#444}
.testimonial-name{position:absolute;left:377px;top:185px;font-size:20px;color:var(--red);font-weight:600}
.t-arrow{position:absolute;top:121px}

/* Partners */
.partners{height:222px;background:var(--red)}
.partners h2{text-align:center;padding-top:28px;color:var(--white);font-size:26px;font-weight:700;letter-spacing:1px}
.partner-row{position:absolute;top:89px;left:54px;display:flex;gap:34px}
.partner{width:162px;height:98px;background:var(--white);display:flex;align-items:center;justify-content:center;font-weight:700;font-size:20px;color:#222;text-align:center}
.partner.narrow{width:132px}

/* Footer */
.site-footer{height:343px;background:var(--footer);color:var(--white)}
.f-brand{position:absolute;left:58px;top:22px}
.f-brand-mark{width:44px;height:44px;border-radius:50%;background:var(--white);margin-left:18px}
.f-brand-name{font-weight:700;font-size:14px;line-height:16px;margin-top:6px;width:90px}
.f-contact{position:absolute;left:50px;top:125px;font-size:12.5px;line-height:19px}
.f-contact div{display:flex;gap:10px;margin-bottom:12px}
.f-col{position:absolute;top:52px}
.f-col h4{font-size:16px;font-weight:700;letter-spacing:1px;margin-bottom:26px}
.f-col li{list-style:none;font-size:12.5px;line-height:20px;color:#ddd}
.f-sitemap{left:281px}.f-services{left:478px}.f-follow{left:704px}.f-subscribe{left:915px}
.f-social{display:flex;gap:8px}
.f-social span{width:36px;height:36px;border:1px solid #777;display:flex;align-items:center;justify-content:center}
.f-social i{width:14px;height:14px;border-radius:50%;background:var(--white)}
.f-subscribe p{font-size:12.5px;line-height:20px;color:#ddd;width:220px}
.f-email{margin-top:28px;width:228px;height:34px;background:var(--white);display:flex;align-items:center;justify-content:space-between;padding:0 14px;color:#999;font-size:12px}
.bottom-bar{position:absolute;left:0;bottom:0;width:1200px;height:41px;background:var(--blue);color:var(--white);font-size:12px;font-weight:600;display:flex;align-items:center;justify-content:space-between;padding:0 56px}
</style>
</head>
<body>

<header class="site-header">
  <div class="brand"><span class="brand-dot"></span><span class="brand-name">Brellow Publishing</span></div>
  <nav class="nav-bar">
    <a class="active">Home</a><a>Publishing</a><a>Submissions</a><a>Books</a><a>Authors</a><a>Seminars</a><a>Contact</a>
    <span class="nav-tools">
      <svg width="18" height="18" viewBox="0 0 18 18"><circle cx="7.5" cy="7.5" r="5.5" fill="none" stroke="#fff" stroke-width="2"/><line x1="11.5" y1="11.5" x2="16" y2="16" stroke="#fff" stroke-width="2.5"/></svg>
      <svg width="2" height="26"><rect width="2" height="26" fill="#fff"/></svg>
      <svg width="24" height="22" viewBox="0 0 24 22"><path d="M1 2h4l3 12h12l2-9H7" fill="none" stroke="#fff" stroke-width="2"/><circle cx="9" cy="19" r="2" fill="#fff"/><circle cx="18" cy="19" r="2" fill="#fff"/></svg>
    </span>
  </nav>
</header>

<section class="hero">
  <div class="hero-photo" role="img" aria-label="Photo of a smiling woman working on a laptop at a desk"></div>
  <div class="social-bar"><span aria-label="Social link"><i></i></span><span aria-label="Social link"><i></i></span><span aria-label="Social link"><i></i></span></div>
  <div class="social-toggle">‹</div>
  <div class="hero-title">
    <h1>BRELLOW PUBLICATIONS</h1>
    <p>SELF-PUBLISHING THAT WORK</p>
  </div>
  <div class="btn-submit">SUBMIT WORK</div>
</section>

<section class="intro">
  <h2>HAVE A STORY TO TELL? WE CAN HELP YOU PUBLISH YOUR BOOK.</h2>
  <p>Welcome to BRELLOW PUBLISHING, we are an independent publishing company located in London/Surrey. We publish TRADE (fiction and non-fiction), &amp; YOUNG ADULT (YA)<br>in a variety of subjects.</p>
  <div class="feature-cards">
    <div class="card card-books">
      <svg width="92" height="80" viewBox="0 0 92 80"><path d="M46 0L92 16 46 32 0 16z" fill="#ec1f27"/><path d="M0 32l46 16 46-16v12L46 60 0 44z" fill="#ec1f27"/><path d="M0 52l46 16 46-16v12L46 80 0 64z" fill="#ec1f27"/></svg>
      BOOKS
    </div>
    <div class="card card-author">
      <svg width="100" height="80" viewBox="0 0 100 80"><rect x="2" y="2" width="96" height="76" fill="none" stroke="#fff" stroke-width="4"/><circle cx="28" cy="30" r="10" fill="#fff"/><path d="M12 64c0-14 32-14 32 0z" fill="#fff"/><rect x="54" y="18" width="34" height="6" fill="#fff"/><rect x="54" y="32" width="34" height="6" fill="#fff"/><rect x="54" y="46" width="34" height="6" fill="#fff"/></svg>
      AUTHOR
    </div>
    <div class="card card-submission">
      <svg width="70" height="84" viewBox="0 0 70 84"><rect x="2" y="2" width="52" height="68" fill="none" stroke="#fff" stroke-width="3"/><rect x="14" y="12" width="54" height="70" fill="#8cc63f" stroke="#fff" stroke-width="3"/><path d="M26 44l10 10 20-22" fill="none" stroke="#fff" stroke-width="5"/></svg>
      SUBMISSION
    </div>
  </div>
</section>

<section class="video">
  <div class="video-still" role="img" aria-label="Video still of hands typing on a laptop keyboard"></div>
  <svg class="play" width="132" height="132" viewBox="0 0 132 132"><circle cx="66" cy="66" r="62" fill="none" stroke="#fff" stroke-width="6"/><path d="M50 36l44 30-44 30z" fill="#fff"/></svg>
  <h2>LEARN HOW WE PUBLISH BOOKS</h2>
</section>

<section class="steps">
  <div class="step step-writing">
    <svg width="80" height="80" viewBox="0 0 80 80"><path d="M60 4l16 16-40 40-22 6 6-22z" fill="#ec1f27"/><path d="M8 72h30" stroke="#ec1f27" stroke-width="4"/></svg>
    <h3>WRITING</h3>
    <p>You write a book to the best of your ability And after redrafting several times when you honestly feel that you have done the best you Possibly can with it, you send it to us</p>
  </div>
  <div class="step step-review">
    <svg width="96" height="80" viewBox="0 0 96 80"><rect x="4" y="4" width="62" height="44" fill="none" stroke="#ec1f27" stroke-width="5"/><path d="M14 48v14l12-14" fill="#ec1f27"/><rect x="30" y="22" width="62" height="44" fill="#ec1f27"/><path d="M80 66v12L68 66" fill="#ec1f27"/><rect x="40" y="34" width="42" height="4" fill="#fff"/><rect x="40" y="46" width="42" height="4" fill="#fff"/></svg>
    <h3>REVIEW</h3>
    <p>You send us your book and our editorial team will look over it and decide if we like it and</p>
  </div>
  <div class="steps-panel">
    <h2>PUBLISH YOUR BOOK IN<br><em>4</em> EASY STEPS</h2>
    <ul>
      <li>You submit your manuscript to us for review.</li>
      <li>Within 6 weeks we will make a decision and contact you to let you know our decision.</li>
      <li>If we like it we will meet and discuss a contract. This includes deadlines, royalty payments, and other options.</li>
      <li>When the book is published we take care of the marketing and sales for you.</li>
      <li>You become a published author and enjoy the financial rewards.</li>
    </ul>
    <p class="more">For more details please See <span>here</span></p>
  </div>
  <div class="step step-submission">
    <svg width="90" height="80" viewBox="0 0 90 80"><path d="M6 44l22 24L84 6" fill="none" stroke="#ec1f27" stroke-width="14" stroke-linecap="round"/></svg>
    <h3>SUBMISSION</h3>
    <p>If your book is in our subject matter and you think you have something that could tickle our fancy, send Us your book for review.</p>
  </div>
  <div class="step step-contract">
    <svg width="84" height="80" viewBox="0 0 84 80"><rect x="4" y="10" width="50" height="64" fill="none" stroke="#ec1f27" stroke-width="5" transform="rotate(-12 29 42)"/><rect x="24" y="6" width="54" height="68" fill="#ec1f27"/><rect x="34" y="20" width="34" height="4" fill="#fff"/><rect x="34" y="32" width="34" height="4" fill="#fff"/><rect x="34" y="44" width="34" height="4" fill="#fff"/><rect x="34" y="56" width="20" height="4" fill="#fff"/></svg>
    <h3>CONTRACT</h3>
    <p>You send us your book and our editorial team will look over it and decide if we like it and then we will Decide what</p>
  </div>
</section>

<section class="books">
  <h2>BOOKS WE HAVE PUBLISHED</h2>
  <div class="arrow-btn arrow-prev"><svg width="20" height="40"><path d="M16 4L4 20l12 16" fill="none" stroke="#777" stroke-width="2"/></svg></div>
  <div class="book-row">
    <div class="cover cover-1" role="img" aria-label="Book cover with a deep red ornamental design"></div>
    <div class="cover cover-2" role="img" aria-label="Book cover illustration of figures by a winding river in a desert"></div>
    <div class="cover cover-3" role="img" aria-label="Book cover with a collage of food and fitness photos"></div>
    <div class="cover cover-4" role="img" aria-label="Book cover with white title lettering on black"></div>
  </div>
  <div class="arrow-btn arrow-next"><svg width="20" height="40"><path d="M4 4l12 16L4 36" fill="none" stroke="#777" stroke-width="2"/></svg></div>
</section>

<section class="testimonials">
  <h2>TESTIMONIALS</h2>
  <svg class="t-arrow" style="left:60px" width="30" height="56"><path d="M26 4L6 28l20 24" fill="none" stroke="#999" stroke-width="3"/></svg>
  <div class="avatar" role="img" aria-label="Portrait photo of the reviewer"></div>
  <div class="quote-badge">“</div>
  <p class="testimonial-text">Lorem Ipsum is simply dummy text of the printing and typesetting industry. Lorem Ipsum has been the industry's standard dummy text ever</p>
  <p class="testimonial-name">–  Mark Ellison</p>
  <svg class="t-arrow" style="left:1110px" width="30" height="56"><path d="M4 4l20 24L4 52" fill="none" stroke="#999" stroke-width="3"/></svg>
</section>

<section class="partners">
  <h2>COMPANIES WE WORK WITH</h2>
  <div class="partner-row">
    <div class="partner narrow">Northleaf</div>
    <div class="partner">Pagewell</div>
    <div class="partner">Inkstand</div>
    <div class="partner">Quillbox</div>
    <div class="partner">Harbor &amp; Vine</div>
    <div class="partner">Leafline</div>
  </div>
</section>

<footer class="site-footer">
  <div class="f-brand"><div class="f-brand-mark"></div><div class="f-brand-name">Brellow Publishing</div></div>
  <div class="f-contact">
    <div><svg width="12" height="16" viewBox="0 0 12 16"><path d="M6 0a6 6 0 0 0-6 6c0 5 6 10 6 10s6-5 6-10a6 6 0 0 0-6-6z" fill="#fff"/><circle cx="6" cy="6" r="2" fill="#2b2b2b"/></svg><span>Brellow Publishing Ltd<br>88-92 Fernhill Road<br>London EC2R 7QT</span></div>
    <div><svg width="14" height="12"><rect width="14" height="10" y="1" fill="#fff"/><path d="M0 1l7 5 7-5" fill="none" stroke="#2b2b2b"/></svg><span>info@brellowpublications.com</span></div>
    <div><svg width="12" height="14" viewBox="0 0 12 14"><path d="M2 0h3l1 4-2 1c1 2 2 3 4 4l1-2 3 1v3c0 1-1 2-2 2C5 13 0 8 0 2 0 1 1 0 2 0z" fill="#fff"/></svg><span>07400 518263</span></div>
  </div>
  <div class="f-col f-sitemap"><h4>SITE MAP</h4><ul><li>Home</li><li>Publishing</li><li>Submissions</li><li>Books</li><li>Authors</li><li>Seminars</li><li>Contact</li></ul></div>
  <div class="f-col f-services"><h4>SERVICES</h4><ul><li>Submission</li><li>Books</li><li>Author</li><li>Production</li><li>Seminars</li><li>Contact</li><li>Ebooks</li><li>Packages</li><li>Career</li></ul></div>
  <div class="f-col f-follow"><h4>FOLLOW US ON</h4><div class="f-social"><span><i></i></span><span><i></i></span><span><i></i></span></div></div>
  <div class="f-col f-subscribe"><h4>SUBSCRIBE</h4><p>Receive updates as they happen.<br>Enter your details</p>
    <div class="f-email">Enter email <svg width="18" height="16" viewBox="0 0 18 16"><path d="M0 7L18 0 14 16 9 10z" fill="#2b2b2b"/></svg></div></div>
  <div class="bottom-bar"><span>Copyright © 2016 ·brellow. All Rights Reserved.</span><span>Terms of Use / Privacy Policy</span></div>
</footer>

</body>
</html>
```